Broschüre für Nachlassverwaltung und Testamentsvollstreckung
Zielgruppe
Nachlassverwaltung und Testamentsvollstreckung
Aufgabenstellung
Ich brauche:
1. ) Präsentationsmappe: mit Visitenkartentasche innenliegend links unten, Endformat: 440 x 307 mm
Endformat: 440 x 307 mm
Seitenanzahl: 2-seitig
Farbigkeit: 4/4-farbig
Diese Beschreibung bezieht sich auf unsere Topseller-Sorte 0,40 mm starker Chromokarton 255g (zertifiziert mit GWNA-Siegel für Nachhaltigkeit), hohe Steifigkeit mit 1,6-fachem Volumen. Weitere Sorten finden Sie in der Produktauswahl.
Hochwertige Mappe für DIN A4, 4/4 farbig (Außen- und Innenseite bedruckt)
0,40 mm starker Chromokarton 255g (zertifiziert mit GWNA-Siegel für Nachhaltigkeit), hohe Steifigkeit mit 1,6-fachem Volumen
Datenformat: 45,0 x 31,7 cm
Endformat: 44,0 x 30,7 cm
2. ) Ringordner
Ringbuch (2-Loch) bis zu 400 DIN A4 Blätter
Außen- und Innenseite farbig bedruckt (4/4)
Hochwertiger Qualitätsdruck mit Glanzfolie veredelt
4/4 farbig außen und innen
Endformat: 61,5 cm x 31,5 cm
geschlossenes Endformat: 28,2 cm x 31,5 cm
Datenformat: 65,1 cm x 35,1 cm
Folgende Dienstleistungen sollten mit aufgeführt sein:
- Testamentsvollstreckung
- Nachlassabwicklung
- Nachlassverwaltung
- Nachlasspflege

```html
<!DOCTYPE html>
<html lang="de">
<head>
<meta charset="UTF-8">
<title>Velden Nachlassmanagement – Präsentationsmappe</title>
<link rel="stylesheet" href="https://fonts.googleapis.com/css2?family=Cinzel:wght@400&family=Roboto:wght@400;500&display=swap">
<style>
  :root {
    --page-bg: #ececec;
    --folder-dark: #474948;
    --paper: #f5f5f4;
    --ink: #2e2e2e;
    --ink-soft: #555555;
    --white: #f4f4f2;
    --accent-line: #8a7d68;
    --badge-fill: #d9d9d7;
    --badge-rim: #b9a57a;
  }
  * { box-sizing: border-box; margin: 0; padding: 0; }
  html, body { width: 1200px; height: 2400px; overflow: hidden; background: var(--page-bg); }
  body { position: relative; font-family: "Roboto", Arial, sans-serif; }
  a, a:visited { color: inherit; text-decoration: none; }

  .spread {
    position: absolute; left: 50px; width: 1100px; height: 768px;
    display: flex; box-shadow: 0 6px 24px rgba(0,0,0,.12);
  }
  .spread--outside { top: 396px; background: var(--folder-dark); }
  .spread--inside { top: 1236px; background: var(--paper); }
  .panel { position: relative; width: 550px; height: 100%; overflow: hidden; }

  /* company name: plain text with one plain circle */
  .company-name {
    position: absolute; display: flex; align-items: center; gap: 10px;
    color: var(--white); font-family: "Roboto", Arial, sans-serif;
    font-weight: 400; font-size: 16px; white-space: nowrap;
  }
  .company-name__dot { width: 10px; height: 10px; border-radius: 50%; background: currentColor; flex: none; }
  .company-name--large { font-size: 21px; }
  .company-name--large .company-name__dot { width: 13px; height: 13px; }
  .company-name--small { font-size: 12px; gap: 7px; }
  .company-name--small .company-name__dot { width: 8px; height: 8px; }
  .company-name--dark { color: var(--ink); }

  /* outside back */
  .back .company-name { top: 78px; right: 60px; }
  .contact { position: absolute; right: 60px; top: 532px; text-align: right; color: var(--white); font-size: 11.5px; line-height: 1.6; }
  .contact p + p { margin-top: 6px; }
  .back__rule { position: absolute; left: 38px; right: 60px; top: 667px; border-top: 1px solid var(--accent-line); }
  .membership { position: absolute; left: 38px; top: 690px; color: var(--white); font-size: 13px; line-height: 1.2; }
  .partners { position: absolute; left: 250px; top: 684px; display: flex; gap: 26px; align-items: center; }
  .partner-mark { background: rgba(255,255,255,.28); }
  .partner-mark--wide { width: 72px; height: 28px; }
  .partner-mark--round { width: 42px; height: 42px; border-radius: 50%; background: rgba(255,255,255,.75); }

  /* outside front */
  .front .company-name { top: 76px; right: 60px; }
  .title { position: absolute; left: 52px; top: 552px; color: var(--white); font-family: "Cinzel", Georgia, serif; font-size: 40px; line-height: 1.2; font-weight: 400; }
  .title__rule { position: absolute; left: 52px; top: 668px; width: 92px; border-top: 2px solid var(--accent-line); }
  .award { position: absolute; right: 42px; top: 580px; width: 90px; height: 110px; border-radius: 8px; background: var(--badge-fill); border: 3px solid var(--badge-rim); }

  /* inside left */
  .section-title { font-family: "Cinzel", Georgia, serif; font-weight: 400; color: var(--ink); font-size: 24px; letter-spacing: .5px; }
  .about { position: absolute; left: 40px; top: 40px; width: 470px; }
  .about p { margin-top: 14px; font-size: 11px; line-height: 1.6; color: var(--ink-soft); text-align: justify; }
  .portrait { position: absolute; left: 0; top: 330px; width: 230px; height: 250px; background: linear-gradient(135deg, #d8d8d6 0%, #a9a9a7 55%, #6f6f6d 100%); }
  .services { position: absolute; left: 262px; top: 372px; }
  .services ul { list-style: none; margin-top: 14px; }
  .services li { display: flex; align-items: center; gap: 10px; font-size: 14px; color: var(--ink); margin-bottom: 6px; }
  .services li svg { flex: none; }
  .pocket { position: absolute; left: 0; bottom: 0; }
  .business-card { position: absolute; left: 40px; top: 598px; width: 260px; height: 146px; background: #fbfbfa; clip-path: polygon(0 0, 100% 0, 100% 70%, 88% 100%, 0 100%); }
  .business-card .company-name { top: 62px; left: 28px; }
  .pocket-award { position: absolute; left: 395px; top: 660px; width: 62px; height: 76px; border-radius: 6px; background: var(--badge-fill); border: 2px solid var(--badge-rim); }

  /* inside right */
  .inside-right .company-name { right: 70px; top: 684px; }
</style>
</head>
<body>

<section class="spread spread--outside" aria-label="Mappe außen">
  <div class="panel back">
    <div class="company-name"><span class="company-name__dot"></span>Velden Nachlassmanagement</div>
    <div class="contact">
      <p>Lindenallee 24<br>48153 Musterstadt</p>
      <p>+49 (0) 2500 / 12 34 560<br>info@velden-nachlass.de<br>www.velden-nachlass.de</p>
    </div>
    <div class="back__rule"></div>
    <p class="membership">Mitglied im Verband Deutscher<br>Nachlassbetreuer</p>
    <div class="partners">
      <div class="partner-mark partner-mark--wide"></div>
      <div class="partner-mark partner-mark--wide"></div>
      <div class="partner-mark partner-mark--round"></div>
    </div>
  </div>
  <div class="panel front">
    <div class="company-name company-name--large"><span class="company-name__dot"></span>Velden Nachlassmanagement</div>
    <h1 class="title">Sorgfalt<br>mit Herz</h1>
    <div class="title__rule"></div>
    <div class="award"></div>
  </div>
</section>

<section class="spread spread--inside" aria-label="Mappe innen">
  <div class="panel inside-left">
    <div class="about">
      <h2 class="section-title">Über mich</h2>
      <p>Gerne möchte ich mich Ihnen kurz vorstellen. Seit vielen Jahren begleite ich Familien, Erben und Institutionen in allen Fragen rund um den Nachlass. Als zertifizierte Testamentsvollstreckerin arbeite ich sorgfältig, diskret und mit großem Verantwortungsbewusstsein. Mein Ziel ist es, Ihnen in einer schwierigen Lebensphase Sicherheit zu geben und den letzten Willen zuverlässig umzusetzen. Dabei stehe ich in engem Austausch mit Gerichten, Banken, Behörden und Fachanwälten. Durch regelmäßige Fortbildungen halte ich mein Wissen stets auf dem neuesten Stand. Ich freue mich darauf, Sie kennenzulernen und gemeinsam mit Ihnen den passenden Weg zu finden.</p>
    </div>
    <div class="portrait" role="img" aria-label="Schwarz-Weiß-Porträt der Inhaberin"></div>
    <div class="services">
      <h2 class="section-title">Leistungen</h2>
      <ul>
        <li><svg width="16" height="12" viewBox="0 0 16 12"><path d="M1 6 L6 11 L15 1" fill="none" stroke="#2e2e2e" stroke-width="2"/></svg>Testamentsvollstreckung</li>
        <li><svg width="16" height="12" viewBox="0 0 16 12"><path d="M1 6 L6 11 L15 1" fill="none" stroke="#2e2e2e" stroke-width="2"/></svg>Nachlassabwicklung</li>
        <li><svg width="16" height="12" viewBox="0 0 16 12"><path d="M1 6 L6 11 L15 1" fill="none" stroke="#2e2e2e" stroke-width="2"/></svg>Nachlassverwaltung</li>
        <li><svg width="16" height="12" viewBox="0 0 16 12"><path d="M1 6 L6 11 L15 1" fill="none" stroke="#2e2e2e" stroke-width="2"/></svg>Nachlasspflege</li>
      </ul>
    </div>
    <svg class="pocket" width="550" height="200" viewBox="0 0 550 200" aria-hidden="true">
      <path d="M0 0 H460 Q500 0 505 60 L520 200 H0 Z" fill="#474948"/>
    </svg>
    <div class="business-card">
      <div class="company-name company-name--small company-name--dark"><span class="company-name__dot"></span>Velden Nachlassmanagement</div>
    </div>
    <div class="pocket-award"></div>
  </div>
  <div class="panel inside-right">
    <svg class="pocket" width="550" height="150" viewBox="0 0 550 150" aria-hidden="true">
      <path d="M0 150 V70 Q5 0 80 0 H550 V150 Z" fill="#474948"/>
    </svg>
    <div class="company-name company-name--large"><span class="company-name__dot"></span>Velden Nachlassmanagement</div>
  </div>
</section>

</body>
</html>
```